Postcard Design

business name: COZY NEST HELPERS. I am a mother of 2 well adjusted, successful teenage boys. I decided to start this company caring for kids who are home sick, unable to go to daycare or school, and when their parent cant stay home with them. I was also a career woman for many years, with no friends available or family nearby to help when i was in an emergency situation for childcare. I know how stressful it can be when a child gets sick suddenly and unexpectedly. I would like to help out those parents in need, that have pressing schedules and a sick child at home that they really want to take care of, but cant due to their work pressures and priorities. I want parents to know that their child is safe and I can help them when in need, at last minute. The design should show the child is safe and well cared for and the parent is at ease, able to accomplish their obligations. I have also founded a nonprofit environmental education program in which I teach children in youth summer camps. I have taught creativity arts combined with science curriculum in kindergarten to 8th grade non-formal teaching for the past 5 years. This is a small community, and many people know me. I will be handing out these postcards to local daycares and people I know.

Industry/Entity Type

Business

```html
<!DOCTYPE html>
<html lang="en">
<head>
<meta charset="utf-8">
<title>Cozy Nest Helpers – Postcards</title>
<link href="https://fonts.googleapis.com/css2?family=Arimo:ital,wght@0,400;0,700;1,400&family=Lora:ital,wght@1,500&display=swap" rel="stylesheet">
<style>
  :root {
    --orange: #de5a27;
    --teal: #1a9aab;
    --grey-text: #6b6b6b;
    --sage: #d3ddb8;
    --butter: #ede4ad;
    --apricot: #f3d5a4;
    --panel: #ffffff;
    --panel-soft: #f6f7f6;
    --page: #ececec;
  }
  * { box-sizing: border-box; margin: 0; padding: 0; }
  html, body { width: 936px; height: 1200px; overflow: hidden; background: var(--page); }
  body { position: relative; font-family: "Arimo", Arial, sans-serif; }

  .postcard {
    position: absolute; width: 664px; height: 516px;
    overflow: hidden; box-shadow: 0 6px 14px rgba(0,0,0,.18);
  }
  .postcard--front { left: 71px; top: 62px; }
  .postcard--back { left: 169px; top: 631px; width: 666px; }

  .backdrop {
    position: absolute; inset: 0;
    background: linear-gradient(180deg, var(--sage) 0%, var(--apricot) 22%, var(--butter) 45%, var(--butter) 100%);
  }

  .title-block {
    position: absolute; background: var(--orange); color: #fff;
    text-align: center; transform: rotate(-1.5deg);
    display: flex; flex-direction: column; justify-content: center;
    box-shadow: 0 3px 6px rgba(0,0,0,.15);
  }
  .title-block__main { font-weight: 700; font-size: 38px; letter-spacing: .5px; line-height: 1.05; }
  .title-block__sub { font-family: "Lora", Georgia, serif; font-style: italic; font-weight: 500; font-size: 46px; line-height: 1.05; }

  .photo { position: absolute; }
  .photo--framed { border: 8px solid #fff; transform: rotate(3deg); box-shadow: 0 4px 10px rgba(0,0,0,.2);
    background: linear-gradient(135deg, #e9ddd0 0%, #c8a27a 40%, #9bb4d2 75%, #eef0f4 100%); }
  .photo--full { background: linear-gradient(160deg, #e8c9bd 0%, #e7d3a3 40%, #f1e4dc 70%, #f7f3f1 100%);
    border-top: 4px solid #fff; border-left: 4px solid #fff; }

  .text-panel { position: absolute; background: var(--panel); }
  .text-panel--back { background: var(--panel-soft); text-align: center; }

  .lead { color: var(--teal); font-size: 19px; }
  .lead--bold { font-weight: 700; line-height: 1.35; }
  .body-copy { color: var(--grey-text); font-style: italic; font-size: 15.5px; line-height: 1.28; }
  .accent { color: var(--orange); font-weight: 700; font-size: 19px; line-height: 1.4; }

  .reassure { position: absolute; display: flex; align-items: center; gap: 16px; }
  .reassure__mark { width: 62px; height: 56px; border-radius: 6px; background: linear-gradient(180deg,#eee,#f2a08d); flex: none; }

  .contact {
    position: absolute; background: var(--orange); color: #fff; text-align: center;
    display: flex; flex-direction: column; justify-content: center; font-weight: 700;
  }
  .contact__name { font-size: 21px; line-height: 1.35; }
  .contact__phone { font-size: 22px; display: flex; align-items: center; justify-content: center; gap: 8px; }
  .phone-icon { width: 22px; height: 22px; }
</style>
</head>
<body>

<section class="postcard postcard--front">
  <div class="backdrop" role="img" aria-label="Soft pastel patterned background"></div>

  <div class="photo photo--framed" style="left:274px; top:40px; width:375px; height:250px;" role="img" aria-label="Photo of a young boy in bed playing doctor with a bandaged teddy bear"></div>

  <div class="title-block" style="left:38px; top:61px; width:248px; height:163px;">
    <span class="title-block__main">COZY NEST</span>
    <span class="title-block__sub">helpers</span>
  </div>

  <div class="text-panel" style="left:14px; top:227px; width:347px; height:300px;">
    <p class="lead" style="position:absolute; left:17px; top:34px;">Caring for kids who...</p>
    <p class="body-copy" style="position:absolute; left:17px; top:66px; width:322px; text-align:justify;">are home sick and unable to go to daycare or school. I provide a service for parents who really would like to stay home with their child, but have obligations that prevent them from staying home.</p>
    <div class="reassure" style="left:20px; top:186px;">
      <div class="reassure__mark" role="img" aria-label="Small winged heart emblem"></div>
      <p class="body-copy" style="width:222px; text-align:center;">I know how stressful it can be when a child gets sick suddenly and unexpectedly.</p>
    </div>
  </div>

  <p class="accent" style="position:absolute; left:400px; top:320px; width:250px; text-align:center;">I can help you<br>at last minute!</p>

  <div class="contact" style="left:383px; top:410px; width:285px; height:110px; border-top:6px solid #fff; border-left:6px solid #fff;">
    <span class="contact__name">Dana Whitfield</span>
    <span class="contact__phone">
      <svg class="phone-icon" viewBox="0 0 24 24" aria-hidden="true"><circle cx="12" cy="12" r="10.5" fill="none" stroke="#fff" stroke-width="2"/><path d="M8.2 6.8c.5-.4 1.2-.3 1.5.2l1 1.7c.3.5.2 1-.2 1.4l-.7.6c.6 1.4 1.6 2.5 3 3.2l.6-.7c.4-.4 1-.5 1.4-.2l1.7 1c.5.3.6 1 .2 1.5l-.8.9c-.6.6-1.500.8-2.300.5-3-1.200-5.200-3.500-6.300-6.400-.3-.8-.1-1.700.5-2.300z" fill="#fff"/></svg>
      (555) 014-2286
    </span>
  </div>
</section>

<section class="postcard postcard--back">
  <div class="backdrop" role="img" aria-label="Soft pastel patterned background"></div>

  <div class="photo photo--full" style="left:380px; top:119px; width:290px; height:400px;" role="img" aria-label="Photo of a caring woman tending to a sick girl resting in bed"></div>

  <div class="text-panel text-panel--back" style="left:15px; top:161px; width:367px; height:262px;">
    <p class="lead lead--bold" style="margin-top:38px;">You don't need to take<br>the day off again.</p>
    <p class="body-copy" style="margin:20px auto 0; width:318px; font-size:15px;">I would like to help out those parents in need, that have pressing schedules and a sick child at home that they really want to take care of, but cant due to their work pressures and priorities.</p>
    <p class="accent" style="margin-top:20px; font-size:17px;">14 years of childcare experience!</p>
  </div>

  <div class="title-block" style="left:39px; top:33px; width:321px; height:136px;">
    <span class="title-block__main" style="font-size:42px;">COZY NEST</span>
    <span class="title-block__sub" style="font-size:48px;">helpers</span>
  </div>

  <div class="contact" style="left:0; top:422px; width:382px; height:94px;">
    <span class="contact__name">Dana Whitfield</span>
    <span class="contact__phone">
      <svg class="phone-icon" viewBox="0 0 24 24" aria-hidden="true"><circle cx="12" cy="12" r="10.5" fill="none" stroke="#fff" stroke-width="2"/><path d="M8.2 6.8c.5-.4 1.2-.3 1.5.2l1 1.7c.3.5.2 1-.2 1.4l-.7.6c.6 1.4 1.6 2.5 3 3.2l.6-.7c.4-.4 1-.5 1.4-.2l1.7 1c.5.3.6 1 .2 1.5l-.8.9c-.6.6-1.5.8-2.3.5-3-1.2-5.2-3.5-6.3-6.4-.3-.8-.1-1.7.5-2.3z" fill="#fff"/></svg>
      (555) 014-2286
    </span>
  </div>
</section>

</body>
</html>
```